Counseling Practice Business Card

I need a professional looking business card incorporating my new logo that was just completed. Card needs to incorporate my name and title, description of my specialty, my address, my phone number, my fax number, my email and my website URL. I need to be able to choose design on/with different paper colors and textures.
I do not have a lot of business card ideas so I am open to anything but I want bold,sharp, clear card without additional designs other than my logo (see attached file info). I am open to different color backgrounds or paper colors including black. I do not like traditional brackets around area codes in phone number or dashes between numbers in phone number. Am open to other ways of presenting including periods between numbers as appropriate. I do not know enough to know what I like yet but I want card to coordinate and work together with my logo. My practice emphasizes natural mental health interventions so any use of color (with background paper color or the blue and green in my logo) that elicits nature is nice. In addition to black, any natural brown or wood looking background might be desirable also. Most of the offerings so far look very similar and boring.

Target Market(s)

Potential therapy clients and other professionals

Contact Information for Business Card

Card information:
Gerald P. Whitcombe, Ph.D.
Licensed Clinical Psychologist
Integrative Health Coach
5214 Ambergate Blvd NW
Suite 815
Duluth, GA 30096
(770) 555-0143 phone
(770) 555-0178 fax
drgeraldwhitcombe@examplemail.net
brightpathwellness.example

Font styles to use
Serif
Sans Serif
Other font styles liked:
• anything that you think looks crisp, clear and easily readable

Requirements
Must have
• Any color used should coordinate with my logo design (see attached files).
• Card should be printed horizontally so top and bottom are longest sides of rectangle.
• Background color or paper color should complement and highlight logo. Do not like a white background. black, grey, brown or any color my logo would blend well with.
Nice to have
• I would like designer to utilize color to highlight letters/name or phone-fax-web symbols.
• Bottom edge of card could be highlighted if appropriate to an idea.
Should not have
• I would NOT want the card to have a pure white background at all.
• No clear cards.
• Cards should be oriented with long sides on bottom and top, NOT sides. DO NOT LIKE THIS THIN TALL ORIENTATION.

```html
<!DOCTYPE html>
<html lang="en">
<head>
<meta charset="utf-8">
<title>Brightpath Wellness – Business Card</title>
<link rel="stylesheet" href="https://fonts.googleapis.com/css2?family=Roboto:wght@400;500;700&display=swap">
<style>
  :root {
    --stage: #2b2b2b;
    --forest: #1f7a3a;
    --ocean: #1f6fb8;
    --ink: #333333;
    --paper: #f3efe6;
    --on-forest: #ffffff;
  }
  * { margin: 0; padding: 0; box-sizing: border-box; }
  html, body {
    width: 1200px; height: 674px; overflow: hidden;
    background: var(--stage);
    font-family: "Roboto", Arial, sans-serif;
  }
  .stage {
    position: relative; width: 1200px; height: 674px;
    display: flex; align-items: center; justify-content: center; gap: 40px;
  }
  .card {
    position: relative; width: 520px; height: 297px; overflow: hidden;
    box-shadow: 0 12px 30px rgba(0,0,0,.5);
  }
  /* Front */
  .card-front { background: var(--forest); color: var(--on-forest); }
  .world-map {
    position: absolute; inset: 24px 30px 30px 30px; border-radius: 40px;
    background: radial-gradient(ellipse at center, rgba(255,255,255,.10), rgba(255,255,255,0) 70%);
  }
  .front-brand {
    position: absolute; left: 0; right: 0; top: 100px;
    display: flex; align-items: center; justify-content: center; gap: 12px;
  }
  .brand-dot { width: 16px; height: 16px; border-radius: 50%; background: currentColor; }
  .brand-name { font-weight: 700; font-size: 34px; letter-spacing: .5px; }
  .front-url {
    position: absolute; left: 0; right: 0; top: 210px; text-align: center;
    font-size: 13px; font-weight: 500;
  }
  /* Back */
  .card-back { background: var(--paper); color: var(--ink); }
  .back-brand {
    position: absolute; right: 30px; top: 36px; color: var(--ocean);
    display: flex; align-items: center; gap: 8px;
  }
  .back-brand .brand-name { font-size: 24px; }
  .back-brand .brand-dot { width: 12px; height: 12px; }
  .rule { position: absolute; height: 1.5px; background: var(--ocean); }
  .rule-top { left: 200px; right: 30px; top: 104px; }
  .rule-mid { left: 30px; right: 150px; top: 196px; }
  .identity { position: absolute; left: 30px; top: 122px; }
  .person-name { color: var(--ocean); font-weight: 700; font-size: 20px; line-height: 1.15; margin-bottom: 2px; }
  .person-title { font-size: 13px; line-height: 1.3; }
  .contacts { position: absolute; left: 30px; right: 24px; top: 206px; font-size: 11.5px; line-height: 1.6; white-space: nowrap; }
  .contacts .label { color: var(--ocean); font-weight: 700; }
  .contacts .web { color: var(--ocean); }
  .edge-band { position: absolute; left: 0; bottom: 0; width: 520px; height: 12px; }
</style>
</head>
<body>
<main class="stage">
  <section class="card card-front">
    <div class="world-map" role="img" aria-label="Faint world map pattern behind the logo"></div>
    <div class="front-brand">
      <span class="brand-dot"></span>
      <span class="brand-name">Brightpath Wellness</span>
    </div>
    <p class="front-url">www.brightpathwellness.example</p>
  </section>

  <section class="card card-back">
    <div class="back-brand">
      <span class="brand-dot"></span>
      <span class="brand-name">Brightpath Wellness</span>
    </div>
    <div class="rule rule-top"></div>
    <div class="identity">
      <p class="person-name">Gerald P. Whitcombe, Ph.D.</p>
      <p class="person-title">Licensed Clinical Psychologist</p>
      <p class="person-title">Integrative Health Coach</p>
    </div>
    <div class="rule rule-mid"></div>
    <div class="contacts">
      <p><span class="label">P</span> : 770.555.0143 | <span class="label">F</span> : 770.555.0178 | <span class="label">E</span> : drgeraldwhitcombe@examplemail.net</p>
      <p><span class="label">W</span> : www.<span class="web">brightpathwellness.example</span></p>
      <p><span class="label">A</span> : 5214 Ambergate Blvd NW Suite 815 Duluth, GA 30096</p>
    </div>
    <svg class="edge-band" viewBox="0 0 520 12" preserveAspectRatio="none" aria-hidden="true">
      <polygon points="0,12 0,6 340,6 336,12" fill="var(--ocean)"/>
      <polygon points="350,12 356,0 520,0 520,12" fill="var(--forest)"/>
    </svg>
  </section>
</main>
</body>
</html>
```